Unique Elegant Stationary Set

Prepare a unique eye catching stationary set consisting of :
(1) Letterhead
(2) A3 Envelope
(3) Business Card
(4) Email Signature Banner

Package to be elegant, modern, and designers not only to think of design or colors but also materials could make a big difference, embossing, debossing, glossy, matt ....etc.

I attached both our new logos (Stacked or Linear) noting you may use any of them but you cant modify anything in the logos. Also attached our final draft portfolio to see what type of projects we work on and i also have here a glimmerboard page link showing the direction we want: https://www.glimmerboard.example/dorvanmelik/business-card-design/

Target Market(s)

VVIP / Elite Developers

Industry/Entity Type

Architecture

Font styles to use
Sans Serif
Other font styles liked:
• unitext

Requirements
Should not have
• too many colors, or being busy in general. We want something pleasing to the eye

```html
<!DOCTYPE html>
<html lang="en">
<head>
<meta charset="utf-8">
<title>Korvel Studio – Business Card</title>
<link rel="stylesheet" href="https://fonts.googleapis.com/css2?family=Open+Sans:wght@300;400;700&display=swap">
<style>
  :root {
    --backdrop: #e4e4e2;
    --card: #f4f4f2;
    --brand-red: #c8202b;
    --text-grey: #4a4a4a;
    --emboss: #e6e6e3;
  }
  * { margin: 0; padding: 0; box-sizing: border-box; }
  html, body {
    width: 1200px; height: 900px; overflow: hidden;
    background: var(--backdrop);
    font-family: "Open Sans", Arial, sans-serif;
  }
  .card-set {
    position: relative; width: 1200px; height: 900px;
  }
  .card {
    position: absolute; top: 135px;
    width: 360px; height: 630px;
    background: var(--card);
  }
  .card--front { left: 180px; }
  .card--back { left: 660px; }

  .brand {
    position: absolute; left: 40px; top: 70px;
    display: flex; align-items: center; gap: 10px;
  }
  .brand__name {
    font-weight: 700; font-size: 30px; letter-spacing: 1px;
    color: var(--brand-red); text-transform: uppercase;
  }
  .brand__square {
    width: 8px; height: 8px; background: var(--brand-red);
    margin-top: 14px;
  }

  .contact {
    position: absolute; left: 40px; bottom: 50px;
    color: var(--text-grey);
  }
  .contact__name {
    font-size: 22px; font-weight: 700; color: var(--brand-red);
    text-transform: uppercase; line-height: 1.1;
  }
  .contact__role { font-size: 16px; margin-bottom: 14px; }
  .contact__address { font-size: 16px; line-height: 1.3; margin-bottom: 14px; }
  .contact__list { list-style: none; font-size: 16px; line-height: 1.5; }
  .contact__list li { display: flex; align-items: center; gap: 8px; }
  .contact__icon { width: 16px; height: 16px; flex: none; }

  .back-mark {
    position: absolute; right: 34px; top: 50%;
    transform: translate(50%, -50%) rotate(90deg);
    transform-origin: center;
    font-weight: 300; font-size: 44px; letter-spacing: 28px;
    color: var(--emboss); text-transform: uppercase; white-space: nowrap;
  }
</style>
</head>
<body>
<main class="card-set">
  <section class="card card--front">
    <div class="brand">
      <span class="brand__name">Korvel Studio</span>
      <span class="brand__square"></span>
    </div>

    <div class="contact">
      <p class="contact__name">Marten Okafor</p>
      <p class="contact__role">Managing Director</p>
      <p class="contact__address">Your Address, City<br>State, Zip 0000</p>
      <ul class="contact__list">
        <li>
          <svg class="contact__icon" viewBox="0 0 16 16" aria-hidden="true">
            <path d="M3 3h3l1 3-2 1a8 8 0 0 0 4 4l1-2 3 1v3c0 1-1 1-1 1A11 11 0 0 1 2 4s0-1 1-1z" fill="var(--brand-red)"/>
          </svg>
          044-555 010 200
        </li>
        <li>
          <svg class="contact__icon" viewBox="0 0 16 16" aria-hidden="true">
            <rect x="1" y="3" width="14" height="10" rx="1" fill="var(--brand-red)"/>
            <path d="M1.5 4 8 9l6.5-5" stroke="#fff" stroke-width="1.3" fill="none"/>
          </svg>
          info@korvelstudio.example
        </li>
        <li>
          <svg class="contact__icon" viewBox="0 0 16 16" aria-hidden="true">
            <circle cx="8" cy="8" r="7" fill="var(--brand-red)"/>
            <ellipse cx="8" cy="8" rx="3" ry="6" stroke="#fff" stroke-width="1" fill="none"/>
            <path d="M2 8h12" stroke="#fff" stroke-width="1"/>
          </svg>
          www.korvelstudio.example
        </li>
      </ul>
    </div>
  </section>

  <section class="card card--back">
    <span class="back-mark">Korvel</span>
  </section>
</main>
</body>
</html>
```